Eine Mieterliste in Apple Numbers erstellen (Vorlage vorhanden)
Zielgruppe
Immobilienverwaltung
Aufgabenstellung
Erstellung einer ansprechenden Mieterliste für eine Mehrfamilienhaus in Apple Numbers
(Excel Vorlage vorhanden als PDF)

```html
<!DOCTYPE html>
<html lang="de">
<head>
<meta charset="utf-8">
<title>Mieterliste Erlenbrück</title>
<link href="https://fonts.googleapis.com/css2?family=Arimo:wght@400;700&display=swap" rel="stylesheet">
<style>
:root{
  --toolbar:#2a2a2a;
  --toolbar-text:#ffffff;
  --tabbar:#f4f4f4;
  --tab-green:#3aa83a;
  --grid:#c9c9c9;
  --grid-dark:#9d9d9d;
  --head-bg:#f2f2f2;
  --head-active:#cfe0f6;
  --head-text:#777;
  --ink:#1a1a1a;
  --select:#4a86d8;
}
*{box-sizing:border-box;margin:0;padding:0}
html,body{width:1200px;height:997px;overflow:hidden;background:#fff}
body{font-family:"Arimo",Helvetica,Arial,sans-serif;color:var(--ink)}
.app{width:924px;height:768px;transform:scale(1.2987);transform-origin:0 0;position:relative}
.toolbar{position:absolute;left:0;top:0;width:924px;height:45px;background:var(--toolbar);color:var(--toolbar-text)}
.app-name{position:absolute;left:11px;top:11px;font-size:20px;color:var(--toolbar-text)}
.tool{position:absolute;top:10px}
.zoom{position:absolute;left:237px;top:10px;width:63px;height:24px;border-radius:4px;background:#3c3c3c;border:1px solid #555;font-size:13px;padding:4px 0 0 10px;color:#fff}
.tabbar{position:absolute;left:0;top:45px;width:924px;height:33px;background:var(--tabbar);border-bottom:1px solid #ddd}
.tab-add{position:absolute;left:10px;top:4px;font-size:22px;color:var(--tab-green);line-height:22px}
.sheet-tab{position:absolute;left:40px;top:0;width:137px;height:33px;background:var(--tab-green);color:#fff;font-size:15px;padding:8px 0 0 9px;white-space:nowrap;overflow:hidden}
.sheet{position:absolute;left:2px;top:102px;width:907px;border-collapse:collapse;table-layout:fixed;font-size:11px}
.sheet td{border:1px solid var(--grid);padding:0 3px;white-space:nowrap;overflow:visible;vertical-align:middle;height:19px}
.sheet .colhead td{height:14px;background:var(--head-bg);color:var(--head-text);font-size:8px;text-align:center;border-color:#d6d6d6}
.sheet .colhead td.active{background:var(--head-active)}
.sheet td.rowhead{background:var(--head-bg);color:var(--head-text);font-size:7px;text-align:center;padding:0;border-color:#d6d6d6}
.caption-row td{height:27px;border:none}
.caption-row td.title{text-align:center;font-size:12px;border-bottom:1px solid var(--grid-dark)}
.num{text-align:right}
.ctr{text-align:center}
.b{font-weight:700}
.wrap{white-space:normal!important;line-height:13px}
.heading{font-size:16px;font-weight:700;text-align:center}
.selected{outline:1.5px solid var(--select);outline-offset:-1px}
.tall td{height:31px}
.scrollbar{position:absolute;left:910px;top:102px;width:6px;height:640px;background:#fafafa}
</style>
</head>
<body>
<div class="app">
  <header class="toolbar">
    <div class="app-name">Rasterwerk</div>
    <svg class="tool" style="left:192px" width="24" height="24" viewBox="0 0 24 24" fill="none" stroke="#fff" stroke-width="1.5"><rect x="2" y="4" width="20" height="16" rx="1"/><line x1="8" y1="4" x2="8" y2="20"/><line x1="2" y1="8" x2="22" y2="8"/></svg>
    <div class="zoom">75% &#9662;</div>
    <svg class="tool" style="left:320px" width="22" height="24" viewBox="0 0 22 24" fill="none" stroke="#fff" stroke-width="1.8"><path d="M7 5 L2 10 L7 15"/><path d="M2 10 H13 a6 6 0 0 1 0 12 H8"/></svg>
    <svg class="tool" style="left:358px" width="22" height="24" viewBox="0 0 22 24" fill="none" stroke="#666" stroke-width="1.8"><path d="M15 5 L20 10 L15 15"/><path d="M20 10 H9 a6 6 0 0 0 0 12 H14"/></svg>
    <svg class="tool" style="left:587px" width="22" height="22" viewBox="0 0 22 22" fill="none" stroke="#fff" stroke-width="1.5"><rect x="2" y="3" width="18" height="16"/><line x1="2" y1="8" x2="20" y2="8"/><line x1="2" y1="13" x2="20" y2="13"/><line x1="8" y1="3" x2="8" y2="19"/><line x1="14" y1="3" x2="14" y2="19"/></svg>
    <svg class="tool" style="left:626px" width="22" height="22" viewBox="0 0 22 22" fill="none" stroke="#fff" stroke-width="1.5"><rect x="3" y="13" width="4" height="7"/><rect x="9" y="8" width="4" height="12"/><rect x="15" y="3" width="4" height="17"/></svg>
    <svg class="tool" style="left:664px" width="22" height="22" viewBox="0 0 22 22" fill="none" stroke="#fff" stroke-width="2"><line x1="3" y1="3" x2="19" y2="3"/><line x1="11" y1="3" x2="11" y2="20"/></svg>
    <svg class="tool" style="left:703px" width="22" height="22" viewBox="0 0 22 22" fill="none" stroke="#fff" stroke-width="1.5"><circle cx="13" cy="8" r="6"/><rect x="3" y="9" width="10" height="10" fill="var(--toolbar)"/><rect x="3" y="9" width="10" height="10"/></svg>
    <svg class="tool" style="left:743px" width="22" height="22" viewBox="0 0 22 22" fill="none" stroke="#fff" stroke-width="1.5"><rect x="2" y="3" width="18" height="16"/><path d="M3 17 L9 10 L13 14 L16 11 L20 15"/><circle cx="15" cy="7" r="1.5"/></svg>
    <svg class="tool" style="left:784px" width="22" height="22" viewBox="0 0 22 22" fill="none" stroke="#fff" stroke-width="1.5"><rect x="4" y="2" width="14" height="18"/><line x1="7" y1="7" x2="15" y2="7"/><line x1="7" y1="11" x2="15" y2="11"/><line x1="7" y1="15" x2="15" y2="15"/></svg>
  </header>

  <nav class="tabbar">
    <div class="tab-add">+</div>
    <div class="sheet-tab">Mieter Erlenbrück..</div>
  </nav>

  <table class="sheet">
    <colgroup>
      <col style="width:17px"><col style="width:39px"><col style="width:119px"><col style="width:98px"><col style="width:71px"><col style="width:130px"><col style="width:37px"><col style="width:28px"><col style="width:59px"><col style="width:45px"><col style="width:70px"><col style="width:73px"><col style="width:121px">
    </colgroup>
    <tr class="colhead"><td></td><td>A</td><td>B</td><td>C</td><td>D</td><td>E</td><td>F</td><td>G</td><td>H</td><td>I</td><td class="active">J</td><td>K</td><td>L</td></tr>
    <tr class="caption-row"><td></td><td class="title" colspan="12">Table 1</td></tr>
    <tr><td class="rowhead">1</td><td></td><td></td><td></td><td></td><td class="heading" colspan="5">Mieter Erlenbrück, Kornblumenweg 35</td><td></td><td></td><td></td></tr>
    <tr><td class="rowhead">2</td><td></td><td></td><td></td><td></td><td></td><td></td><td></td><td></td><td></td><td></td><td></td><td></td></tr>
    <tr><td class="rowhead">3</td><td></td><td class="b">Stand</td><td>01.02.2016</td><td></td><td></td><td></td><td></td><td></td><td></td><td class="selected"></td><td></td><td></td></tr>
    <tr><td class="rowhead">4</td><td class="ctr b">A</td><td class="b">nicht gewerbliche Mieter</td><td></td><td></td><td></td><td></td><td></td><td></td><td></td><td></td><td></td><td></td></tr>
    <tr><td class="rowhead">5</td><td></td><td></td><td></td><td></td><td></td><td></td><td></td><td></td><td></td><td></td><td></td><td></td></tr>
    <tr class="tall"><td class="rowhead">6</td><td></td><td class="b wrap" colspan="8">Nummer des Raumes im Urzeigersinn, Nr. 7 Dach nach vorn mit Raum rechts, also Raum Dach links Nr. 8</td><td></td><td></td><td></td></tr>
    <tr><td class="rowhead">7</td><td></td><td></td><td></td><td class="b">Beginn des</td><td class="b">Umzug</td><td class="b">von</td><td></td><td class="num">allg</td><td>06421-5550147</td><td></td><td class="num">Kaution lt</td><td class="num">Kaution</td></tr>
    <tr><td class="rowhead">8</td><td class="ctr b">Raum</td><td class="b">Name</td><td class="b">Beruf</td><td class="b">Vertrages</td><td class="b">im Haus</td><td class="b">Raum</td><td></td><td></td><td></td><td class="num">Warmmiete</td><td class="num">Vertrag</td><td class="num">gezahlt</td></tr>
    <tr><td class="rowhead">9</td><td class="ctr">APP</td><td>Helene Marwitz</td><td>Ing. Korbach</td><td class="num">01.05.2014</td><td>ohne Strom</td><td></td><td></td><td class="num" colspan="2">0176-55510231</td><td class="num">410,00</td><td class="num">820,00</td><td class="num">14.04.2104</td></tr>
    <tr><td class="rowhead">10</td><td class="ctr">1</td><td>Lara Weidner</td><td>Student</td><td class="num">01.03.2105</td><td></td><td></td><td></td><td></td><td></td><td class="num">240,00</td><td class="num">480,00</td><td class="num">03.03.2015</td></tr>
    <tr><td class="rowhead">11</td><td class="ctr">2</td><td>SabineKroll</td><td>Studentin</td><td class="num">01.09.2012</td><td></td><td></td><td></td><td class="num" colspan="2">0151-55520417</td><td class="num">215,00</td><td class="num">430,00</td><td class="num">17.08.2012</td></tr>
    <tr><td class="rowhead">12</td><td class="ctr">3</td><td>Jonas Feldhaus</td><td>Student</td><td class="num">15.08.2014</td><td></td><td></td><td></td><td class="num" colspan="2">0151-55539802</td><td class="num">260,00</td><td class="num">520,00</td><td class="num">15.08.2014</td></tr>
    <tr><td class="rowhead">13</td><td class="ctr">4</td><td>Nils Ostrop</td><td>Student</td><td class="num">15.01.2016</td><td></td><td></td><td></td><td></td><td></td><td class="num">225,00</td><td class="num">0,00</td><td></td></tr>
    <tr><td class="rowhead">14</td><td></td><td>"Gemeinschaftsraum"</td><td></td><td></td><td></td><td></td><td></td><td></td><td></td><td></td><td class="num">0,00</td><td class="num">keine Kaution</td></tr>
    <tr><td class="rowhead">15</td><td class="ctr">5</td><td>Felix Brandt</td><td>Student</td><td class="num">01.03.2015</td><td></td><td></td><td></td><td class="num" colspan="2">0157-55547163</td><td class="num">260,00</td><td class="num">520,00</td><td class="num">26.02.2015</td></tr>
    <tr><td class="rowhead">16</td><td class="ctr">6</td><td>Mira Lendorf</td><td>Student</td><td class="num">15.01.2016</td><td></td><td></td><td></td><td></td><td></td><td class="num">260,00</td><td class="num">520,00</td><td class="num">13.01.2016</td></tr>
    <tr><td class="rowhead">17</td><td class="ctr">7</td><td>Henrik Sommer</td><td>Student</td><td class="num">15.04.2015</td><td>umgezogen aus 8, Kaution alt</td><td></td><td></td><td class="num" colspan="2">0157-55561208</td><td class="num">350,00</td><td class="num">530,00</td><td class="num">14.04.2015/1.10.2015</td></tr>
    <tr><td class="rowhead">18</td><td class="ctr">8</td><td>Nils Ostrop</td><td>Student</td><td class="num">01.10.2015</td><td></td><td></td><td></td><td class="num" colspan="2">0176-55572934</td><td class="num">265,00</td><td class="num">530,00</td><td class="num">22.09.2015</td></tr>
    <tr><td class="rowhead">19</td><td class="ctr b">A</td><td></td><td></td><td></td><td></td><td></td><td></td><td></td><td></td><td class="num b">2.485,00</td><td class="num b">4.350,00</td><td></td></tr>
    <tr><td class="rowhead">20</td><td></td><td></td><td></td><td></td><td></td><td></td><td></td><td></td><td></td><td></td><td></td><td></td></tr>
    <tr><td class="rowhead">21</td><td></td><td></td><td></td><td></td><td></td><td></td><td></td><td></td><td></td><td></td><td></td><td></td></tr>
    <tr><td class="rowhead">22</td><td class="ctr b">B</td><td class="b">gewerblicher Mieter: Laden/Büro</td><td></td><td></td><td></td><td></td><td></td><td></td><td></td><td></td><td></td><td></td></tr>
    <tr><td class="rowhead">23</td><td></td><td></td><td></td><td></td><td></td><td></td><td></td><td></td><td></td><td></td><td></td><td></td></tr>
    <tr><td class="rowhead">24</td><td></td><td colspan="2">Petra Wolken,Karl Ebert Einzelhandel</td><td class="num">15.03.2004</td><td></td><td class="num">Miete</td><td colspan="3">zuzüglich Umsatzsteuer</td><td class="num">1.276,00</td><td class="num">3.300,00</td><td class="num">30.06.04</td></tr>
    <tr><td class="rowhead">25</td><td></td><td>Wichtelhaus GbR</td><td></td><td></td><td></td><td class="num">NK</td><td colspan="3">zuzüglich Umsatzsteuer</td><td class="num">105,00</td><td></td><td></td></tr>
    <tr><td class="rowhead">26</td><td></td><td></td><td></td><td></td><td></td><td></td><td></td><td></td><td></td><td class="num">1.381,00</td><td></td><td></td></tr>
    <tr><td class="rowhead">27</td><td></td><td></td><td></td><td></td><td></td><td></td><td></td><td></td><td>0,19</td><td class="num">262,39</td><td></td><td></td></tr>
    <tr class="tall"><td class="rowhead">28</td><td></td><td></td><td></td><td></td><td></td><td></td><td></td><td></td><td class="wrap" style="vertical-align:top;padding-top:3px">Laden brutto</td><td class="num" style="vertical-align:top;padding-top:3px">1.643,39</td><td></td><td></td></tr>
    <tr><td class="rowhead">29</td><td></td><td></td><td></td><td></td><td></td><td></td><td></td><td></td><td></td><td></td><td></td><td></td></tr>
    <tr><td class="rowhead">30</td><td></td><td></td><td></td><td></td><td></td><td></td><td></td><td></td><td class="b" colspan="2">Summe Kautionen</td><td class="num b">7.650,00</td><td></td></tr>
  </table>
  <div class="scrollbar"></div>
</div>
</body>
</html>
```